Professional DJ Business Card

Business card for giving out to clubs and venues or interested groups that are in need of a professional DJ. I want something artistic and catchy/alluring, with a minimalist approach that gets just the vital amount of info and leaves the rest for inquiry via contacting me. Ideally I would like one side to have an image of something cool like an eye and my name, then the other side be the contact info, I am definitely feeling a black or dark colored card, but I am open to other designs. I am uploading a picture that I made that reflects a little of what I am *kind of* looking for.

Industry/Entity Type

Business

Contact Information for Business Card

Tomas Halvik (Voxtel)
Professional DJ (West Coast)
EDM (Deep/House/Techno), Hip Hop, Latin, Trap.
Cell: 555-274-9163
Email: Voxtelofficial@mailnest.net
www.beatcloudia.net/yourtuneisfading

```html
<!DOCTYPE html>
<html lang="en">
<head>
<meta charset="utf-8">
<title>Tomas Halvik (Voxtel) – Business Card</title>
<link href="https://fonts.googleapis.com/css2?family=Advent+Pro:wght@600&display=swap" rel="stylesheet">
<style>
  :root {
    --card-black: #060708;
    --accent-rose: #d9566f;
    --text-blush: #f7dde2;
    --motif-grey: #5c5f63;
  }
  html, body {
    margin: 0;
    padding: 0;
    width: 1200px;
    height: 702px;
    overflow: hidden;
    background: var(--card-black);
  }
  .card {
    position: relative;
    width: 1200px;
    height: 702px;
    background: var(--card-black);
    overflow: hidden;
    font-family: "Advent Pro", "Arial Narrow", sans-serif;
    font-weight: 600;
    text-transform: uppercase;
    color: var(--text-blush);
  }
  .card__top-rule {
    position: absolute;
    top: 0;
    left: 0;
    width: 100%;
    height: 2px;
    background: var(--accent-rose);
  }
  .card__eye-motif {
    position: absolute;
    left: 0;
    bottom: 0;
    width: 1200px;
    height: 300px;
    background:
      radial-gradient(ellipse 330px 140px at 260px 300px, rgba(92,95,99,0.55), rgba(92,95,99,0) 100%),
      linear-gradient(168deg, rgba(92,95,99,0) 40%, rgba(92,95,99,0.18) 60%, rgba(92,95,99,0) 80%);
  }
  .card__name {
    position: absolute;
    top: 138px;
    left: 0;
    width: 100%;
    margin: 0;
    text-align: center;
    font-size: 33px;
    letter-spacing: 1.5px;
    font-weight: 600;
  }
  .card__details {
    position: absolute;
    top: 250px;
    left: 0;
    width: 100%;
    margin: 0;
    padding: 0;
    list-style: none;
    text-align: center;
    font-size: 28px;
    letter-spacing: 1px;
  }
  .card__details li {
    height: 55.5px;
    line-height: 40px;
  }
</style>
</head>
<body>
  <main class="card">
    <div class="card__top-rule"></div>
    <div class="card__eye-motif" role="img" aria-label="Stylised grey eye with long sweeping lashes in the lower left corner"></div>
    <h1 class="card__name">Tomas Halvik (Voxtel)</h1>
    <ul class="card__details">
      <li class="card__role">Professional DJ (West Coast)</li>
      <li class="card__genres">EDM (Deep/House/Techno), Hip Hop, Latin, Trap</li>
      <li class="card__phone">Cell: 555-274-9163</li>
      <li class="card__email">Email: Voxtelofficial@mailnest.net</li>
      <li class="card__web">www.beatcloudia.net/yourtuneisfading</li>
    </ul>
  </main>
</body>
</html>
```